Wendlemoor Vapes labels

We need a label designed for our e-liquid that we will be selling from our store. (E-liquid is used in electronic cigarettes) The label should be 1-1.5 inches tall and ~3 inches long.

Try to focus on highlighting the name brand over the specific flavor.

Bottle size will be 15ml clear bottles.

There will be 10+ flavors and each flavor will need a slightly different label (with the same overall theme) and different nicotine levels varying from 0mg, 6mg, 12mg, and 18mg.

Initial favor list is:
Coral Drift
Velvet Slosh
Tart Currants
Crakle Plums
Papaya Riot
Zingy Drops
Amber Gryphon
Fizzleleaf
Emberlash
Orvin
Nutmeg Twist

Please add the following warning in caps and small font:

(WHITE FONT)
This product contains nicotine or was produced at a facility that processes nicotine which has been known to cause birth defects and other reproductive harm. This product also contains VG/PG and artificial flavors. Not for sale to minors.
(RED FONT)
Toxic if swallowed or has contact with skin. Keep locked up and out of reach of children and pets. In case of accident or you feel unwell seek medical advice immediately.

young adults

Electronic

```html
<!DOCTYPE html>
<html lang="en">
<head>
<meta charset="utf-8">
<title>Wendlemoor Vapes – e-liquid label</title>
<link rel="stylesheet" href="https://fonts.googleapis.com/css2?family=Libre+Baskerville:wght@400;700&display=swap">
<style>
  :root {
    --backdrop: #1a120c;
    --frame-green: #0e7a1a;
    --header-green: #6f9e32;
    --tab-green: #86a52e;
    --label-white: #ffffff;
    --warning-blue: #0a84e8;
    --warning-red: #e00000;
    --nicotine-grey: #555555;
    --flavor-green: #0d4d14;
  }
  * { margin: 0; padding: 0; box-sizing: border-box; }
  html, body {
    width: 1200px; height: 1000px; overflow: hidden;
    background: var(--backdrop);
    font-family: "Libre Baskerville", Georgia, serif;
  }
  .canvas { position: relative; width: 1200px; height: 1000px; }
  .label {
    position: absolute; left: 151px; top: 276px;
    width: 898px; height: 448px;
    background: var(--label-white);
    border: 6px solid var(--frame-green);
  }
  .label-header {
    position: absolute; left: 0; top: 0; right: 0; height: 110px;
    background: var(--header-green);
  }
  .brand {
    position: absolute; left: 300px; top: 20px; width: 300px;
    display: flex; align-items: center; gap: 14px;
    color: var(--label-white); font-weight: 700; font-size: 28px;
    line-height: 35px; white-space: nowrap;
  }
  .brand-dot {
    width: 22px; height: 22px; border-radius: 50%;
    background: var(--label-white); flex: none;
  }
  .brand-name span { display: block; }
  .flavor-tab {
    position: absolute; left: 626px; top: 24px; width: 249px; height: 86px;
    background: var(--tab-green); border-radius: 10px 10px 0 0;
    color: var(--label-white); font-size: 19px;
    padding: 36px 0 0 22px; white-space: nowrap;
  }
  .warning-white {
    position: absolute; left: 16px; top: 118px; width: 256px; height: 110px;
    background: var(--warning-blue); border-radius: 10px;
    color: var(--label-white); font-size: 9.6px; font-weight: 700;
    line-height: 13.2px; padding: 3px 8px 0 24px;
  }
  .warning-red {
    position: absolute; left: 20px; top: 337px; width: 250px;
    color: var(--warning-red); font-size: 9px; font-weight: 700;
    line-height: 12.5px; text-align: center;
  }
  .center-mark {
    position: absolute; left: 340px; top: 130px; width: 200px; height: 200px;
  }
  .nicotine-levels {
    position: absolute; left: 324px; top: 350px; width: 270px;
    color: var(--nicotine-grey); font-size: 11px; font-weight: 700;
    line-height: 15px; white-space: nowrap;
  }
  .nicotine-levels span { display: block; padding-left: 22px; }
  .flavor-list {
    position: absolute; left: 680px; top: 124px; list-style: none;
    color: var(--flavor-green); font-size: 17px; line-height: 24.6px;
    white-space: nowrap;
  }
</style>
</head>
<body>
<div class="canvas">
  <section class="label">
    <header class="label-header">
      <div class="brand"><span class="brand-dot"></span><div class="brand-name"><span>Wendlemoor</span><span>Vapes</span></div></div>
      <div class="flavor-tab">Initial favor list is:</div>
    </header>

    <p class="warning-white">This product contains nicotine or was produced at a facility that processes nicotine which has been known to cause birth defects and other reproductive harm.<br>This product also contains VG/PG and artificial flavors.<br>Not for sale to minors.</p>

    <p class="warning-red">Toxic if swallowed or has contact with skin.<br>Keep locked up and out of reach of children and pets.<br>In case of accident or you feel<br>unwell seek medical advice immediately.</p>

    <svg class="center-mark" viewBox="0 0 200 200" aria-hidden="true">
      <defs>
        <radialGradient id="halo" cx="50%" cy="50%" r="50%">
          <stop offset="0%" stop-color="#cfe3bd"/>
          <stop offset="70%" stop-color="#e8f2de"/>
          <stop offset="100%" stop-color="#ffffff"/>
        </radialGradient>
      </defs>
      <circle cx="100" cy="110" r="80" fill="url(#halo)"/>
    </svg>

    <p class="nicotine-levels">Different nicotine levels varying from<span>0mg, 6mg, 12mg, and 18mg.</span></p>

    <ul class="flavor-list">
      <li>Coral Drift</li>
      <li>Velvet Slosh</li>
      <li>Tart Currants</li>
      <li>Crakle Plums</li>
      <li>Papaya Riot</li>
      <li>Zingy Drops</li>
      <li>Amber Gryphon</li>
      <li>Fizzleleaf</li>
      <li>Emberlash</li>
      <li>Orvin</li>
      <li>Nutmeg Twist</li>
    </ul>
  </section>
</div>
</body>
</html>
```